Elegant Business Card for Technology Company

Client is a supplier of innovative industrial communications and automation equipment since 2002. This contest is to gather fresh ideas for a redesign of the existing business card. Client is looking for design that best communicates tagline "Industrial Networking and Computing Specialist".

Design submissions should look modern, clean, elegant and professional. It should not be cluttered. Use white as the primary colour. Orange and black as secondary colour. Refer to jpeg File 1 on the current design.

Fonts used by Client used include Arial Regular, Arial Black, Roboto Regular, Roboto Black and Lato.

The winning design will be sent for offset printing using super white 250gsm artcard paper (open for suggestions).

Target Market(s)

System Engineers, Project Managers, Purchasing Managers from companies providing engineering services for Smart Cities.

Industry/Entity Type

Information Technology

Contact Information for Business Card

Refer to PDF File 3 for Business Card Details. Priority of short contact information would be as follows Name > Job Title > Email > Mobile > Web > Tel > Fax > Business Address >UEN (UEN represents company registration number)

Font styles to use
Sans Serif

Colors
ffffff
f37122
000000
5c5c5c

Requirements
Must have
• Refer to AI File 2 (Company Logo) & PDF File 3 (Information on Namecard)
Should not have
• No QR codes
• No Social Media Icons
• Do not create full Black or Orange colour background

```html
<!DOCTYPE html>
<html lang="en">
<head>
<meta charset="utf-8">
<title>QVR Business Card</title>
<link rel="stylesheet" href="https://fonts.googleapis.com/css2?family=Source+Sans+3:wght@400;600;700;800&display=swap">
<style>
  :root {
    --white: #ffffff;
    --orange: #e8731f;
    --black: #000000;
    --grey: #5c5c5c;
    --accent-red: #c8161d;
    --stage: #e9e9e9;
    --card-shade: #f3f3f3;
  }
  * { box-sizing: border-box; margin: 0; padding: 0; }
  html, body {
    width: 1200px; height: 1023px; overflow: hidden;
    background: var(--stage);
    font-family: "Source Sans 3", sans-serif;
  }
  .canvas { position: relative; width: 1200px; height: 1023px; }
  .card {
    position: absolute; width: 620px; height: 354px;
    border-radius: 26px; overflow: hidden;
    background: linear-gradient(160deg, var(--white) 40%, var(--card-shade));
    box-shadow: 0 10px 28px rgba(0,0,0,.18), 0 2px 4px rgba(0,0,0,.12);
  }
  .card--front { left: 290px; top: 110px; }
  .card--back { left: 290px; top: 559px; }

  .brand { position: absolute; display: flex; align-items: center; gap: 14px; }
  .brand__dot { border-radius: 50%; background: var(--orange); }
  .brand__name { font-weight: 800; color: var(--black); letter-spacing: 2px; line-height: 1; }

  .card--front .brand { left: 52px; top: 128px; }
  .card--front .brand__dot { width: 38px; height: 38px; }
  .card--front .brand__name { font-size: 64px; }

  .divider { position: absolute; left: 290px; top: 40px; width: 1.5px; height: 196px; background: var(--black); }
  .divider::before { content: ""; position: absolute; left: -0.5px; top: 0; width: 2.5px; height: 34px; background: var(--accent-red); }

  .contact { position: absolute; left: 318px; top: 36px; color: var(--black); }
  .contact__name { font-size: 27px; font-weight: 600; color: var(--orange); line-height: 1.05; }
  .contact__title { font-size: 16px; margin-bottom: 12px; }
  .contact__list { list-style: none; font-size: 15px; line-height: 20px; }
  .contact__list li { display: flex; align-items: center; gap: 9px; }
  .contact__list svg { width: 13px; height: 13px; fill: var(--orange); flex: none; }
  .contact__address { font-size: 14px; line-height: 18px; margin-top: 10px; }

  .swoosh { position: absolute; inset: 0; width: 620px; height: 354px; }
  .uen { position: absolute; left: 28px; bottom: 12px; color: var(--white); font-size: 14px; letter-spacing: .5px; }

  .band { position: absolute; left: 46px; top: 0; width: 76px; height: 354px; background: var(--orange);
          border-left: 2px solid var(--black); border-right: 2px solid var(--black); }
  .tagline { position: absolute; left: 84px; top: 28px; transform-origin: 0 0; transform: rotate(90deg) translateY(-50%);
             white-space: nowrap; color: var(--white); font-size: 14px; letter-spacing: .2px; }
  .card--back .brand { left: 250px; top: 136px; }
  .card--back .brand__dot { width: 50px; height: 50px; }
  .card--back .brand__name { font-size: 84px; }
</style>
</head>
<body>
<main class="canvas">

  <section class="card card--front" aria-label="Business card front">
    <svg class="swoosh" viewBox="0 0 620 354" aria-hidden="true">
      <path d="M0,298 C220,298 450,306 556,274 C604,256 612,150 620,40 L620,354 L0,354 Z" fill="var(--black)"/>
      <path d="M0,311 C230,311 460,320 566,288 C610,270 616,170 620,80 L620,354 L0,354 Z" fill="var(--orange)"/>
    </svg>

    <div class="brand">
      <span class="brand__dot"></span>
      <span class="brand__name">QVR</span>
    </div>

    <div class="divider"></div>

    <div class="contact">
      <p class="contact__name">Daniel Koh</p>
      <p class="contact__title">Sales Manager</p>
      <ul class="contact__list">
        <li><svg viewBox="0 0 12 12"><rect x="3" y="0" width="6" height="12" rx="1"/></svg>+65 9123 4567</li>
        <li><svg viewBox="0 0 12 12"><path d="M1,2 C1,1 2,0 3,1 L4.5,3 C5,4 4,4.5 4,5 C4.5,6.5 5.5,7.5 7,8 C7.5,8 8,7 9,7.5 L11,9 C12,10 11,11 10,11 C5,11 1,7 1,2 Z"/></svg>+65 6123 4500</li>
        <li><svg viewBox="0 0 12 12"><rect x="0" y="4" width="12" height="8" rx="1"/><rect x="2" y="0" width="8" height="5"/></svg>+65 6123 4511</li>
        <li><svg viewBox="0 0 12 12"><path d="M0,2 H12 V10 H0 Z M0,2 L6,7 L12,2" /></svg>sales@qvr-example.sg</li>
        <li><svg viewBox="0 0 12 12"><circle cx="6" cy="6" r="6"/></svg>info@qvr-example.sg</li>
      </ul>
      <p class="contact__address">22 Harbour Lane, Bayview Park #04-12<br>(Block B), Singapore 418220</p>
    </div>

    <p class="uen">UEN NO : 200911045K</p>
  </section>

  <section class="card card--back" aria-label="Business card back">
    <div class="band"></div>
    <p class="tagline">Industrial Networking and Computing Specialist</p>
    <div class="brand">
      <span class="brand__dot"></span>
      <span class="brand__name">QVR</span>
    </div>
  </section>

</main>
</body>
</html>
```